Dental Business Card

I need Dental oriented business cards.
On the front side -
- on the first line, my name:
Dr Marlow Tasker
- on the second line (just underneath):
Doctor of Dental Medicine
- on the third line, or underneath that or in a corner, I would like the address and phone number:
5192 Ch. Birchfield
Montreal QC H2P 4K8
514-629-5074
- other than that i would maybe like a logo of a tooth, but i want it to be subtle and very basic!
- I would like the card to be preferably black or dark grey-ish with the writing in white
On the other side -
- 2-3 lines with the possibility to write the next appointment the box with the lines should be white, with the rest of the card being black

```html
<!DOCTYPE html>
<html lang="en">
<head>
<meta charset="utf-8">
<title>Dr Marlow Tasker – Business Card</title>
<link href="https://fonts.googleapis.com/css2?family=Jost:wght@400;500&display=swap" rel="stylesheet">
<style>
  :root {
    --backdrop: #e4e5e7;
    --card-dark: #1e1f20;
    --card-mid: #2c2d2f;
    --blue-deep: #0a84cc;
    --blue-light: #3bb9e6;
    --text-white: #ffffff;
  }
  * { box-sizing: border-box; margin: 0; padding: 0; }
  html, body {
    width: 1200px; height: 1200px; overflow: hidden;
    background: var(--backdrop);
    font-family: "Jost", "Futura", sans-serif;
  }
  .canvas {
    width: 1200px; height: 1200px;
    display: flex; flex-direction: column; align-items: center; justify-content: center;
    gap: 60px;
  }
  .card {
    position: relative;
    width: 700px; height: 400px;
    border-radius: 22px;
    overflow: hidden;
    background: linear-gradient(135deg, var(--card-dark) 0%, var(--card-mid) 100%);
    color: var(--text-white);
    box-shadow: 0 12px 30px rgba(0,0,0,0.25);
  }

  /* Front */
  .front-band {
    position: absolute; left: 0; right: 0; bottom: 0; height: 90px;
    background: linear-gradient(90deg, var(--blue-deep) 0%, var(--blue-light) 100%);
  }
  .identity {
    position: absolute; top: 100px; left: 150px;
    display: flex; align-items: center; gap: 26px;
    white-space: nowrap;
  }
  .practice-mark {
    display: flex; align-items: center; gap: 10px;
    font-size: 26px; font-weight: 500; color: var(--blue-light);
    letter-spacing: 0.5px;
  }
  .practice-mark .dot {
    width: 14px; height: 14px; border-radius: 50%; background: var(--blue-light);
  }
  .divider { width: 1.5px; height: 110px; background: var(--blue-light); }
  .details { line-height: 1.25; }
  .doctor-name {
    font-size: 24px; font-weight: 500; color: var(--blue-light);
    text-transform: uppercase; letter-spacing: 0.5px;
  }
  .doctor-title { font-size: 15px; margin-bottom: 10px; }
  .contact-row { display: flex; gap: 7px; font-size: 14px; align-items: flex-start; }
  .contact-row svg { flex: none; margin-top: 3px; }

  /* Back */
  .top-band {
    position: absolute; top: 0; left: 0; right: 0; height: 26px;
    background: var(--blue-light);
  }
  .appointment-heading {
    position: absolute; top: 78px; left: 44px;
    font-size: 25px; font-weight: 400; color: var(--blue-light);
  }
  .field { position: absolute; display: flex; align-items: flex-end; gap: 10px; font-size: 17px; }
  .field .line { height: 0; border-bottom: 2px solid var(--text-white); margin-bottom: 4px; }
  .field-name { top: 142px; left: 44px; }
  .field-date { top: 200px; left: 44px; }
  .field-time { top: 200px; left: 352px; }
  .meridiem { position: absolute; top: 252px; left: 478px; display: flex; gap: 26px; font-size: 18px; }
  .choice { display: flex; align-items: center; gap: 8px; }
  .choice .box { width: 26px; height: 26px; background: var(--text-white); }
  .back-address {
    position: absolute; bottom: 40px; left: 44px;
    font-size: 17px; font-weight: 500;
  }
</style>
</head>
<body>
<main class="canvas">

  <section class="card card-front" aria-label="Card front">
    <div class="front-band" role="img" aria-label="Decorative sweeping blue wave band"></div>
    <div class="identity">
      <div class="practice-mark"><span class="dot"></span>Tasker Dental</div>
      <div class="divider"></div>
      <div class="details">
        <h1 class="doctor-name">Dr Marlow Tasker</h1>
        <p class="doctor-title">Doctor of Dental Medicine</p>
        <p class="contact-row">
          <svg width="10" height="14" viewBox="0 0 10 14"><path d="M5 0a5 5 0 0 1 5 5c0 3.5-5 9-5 9S0 8.5 0 5a5 5 0 0 1 5-5z" fill="var(--blue-light)"/><circle cx="5" cy="5" r="1.8" fill="var(--card-dark)"/></svg>
          <span>5192 Ch. Birchfield<br>Montreal QC H2P 4K8</span>
        </p>
        <p class="contact-row">
          <svg width="12" height="12" viewBox="0 0 12 12"><path d="M2.5 0.5l2 2.5-1.2 1.3a7 7 0 0 0 4.4 4.4L9 7.5l2.5 2-1 2C5.5 11.5 0.5 6.5 0.5 1.5z" fill="var(--blue-light)"/></svg>
          <span>514-629-5074</span>
        </p>
      </div>
    </div>
  </section>

  <section class="card card-back" aria-label="Card back">
    <div class="top-band"></div>
    <h2 class="appointment-heading">Next Appointment</h2>
    <div class="field field-name"><span>Name</span><span class="line" style="width:560px"></span></div>
    <div class="field field-date"><span>Date</span><span class="line" style="width:250px"></span></div>
    <div class="field field-time"><span>Time</span><span class="line" style="width:252px"></span></div>
    <div class="meridiem">
      <span class="choice"><span class="box"></span>AM</span>
      <span class="choice"><span class="box"></span>PM</span>
    </div>
    <p class="back-address">5192 Ch. Birchfield Montreal QC H2P 4K8</p>
  </section>

</main>
</body>
</html>
```